Tri-fold flyer for Wanderbunk Lodge

We would like a new tri fold flyer for our hostel. We've opened up a new location called "Tidewell", and the details and photos of the location can be found at: http://www.harbourlarkstays.com.au/locations/tidewell/
rooms_and_facilities.html. If you have particular types of photos you would like to use we also have a large stock of photos from around the area that we can dig through and make available upon request.
A copy of an old brochure for a different location can be found at: http://www.harbourlarkstays.com.au/marketing/HLS_Tri-fold_Brochure.pdf, however we would like a new design from the ground up.
The flyer should convey a more upmarket image, so it should remain classy/classic - not too "busy" looking, but not boring either. Very chic.
The basic colours must be Purple/Silver/Black. The purple is actually a very specific colour but I assume you can get this from the PDF (otherwise there is an Illustrator file available at http://www.harbourlarkstays.com.au/marketing/HLS_Tri-fold_Brochure.indd). Also, a large version of the logo can be found at http://www.harbourlarkstays.com.au/marketing/logo_source.png if you need it.
Finally, it's important that guests can easily find us so other than the logo a map is about the only absolutely essential element. There is a Google Maps image on our web-site (http://www.harbourlarkstays.com.au/locations/tidewell/contact.html) that explains where we are, but we're sure that this can't be copied to to the flyer for copyright reasons. We would prefer a simpler map anyway.
The important landmarks are:
*Our hostel
*Swiftline bus and Pelican Cay ferry terminal
*Coastlink bus terminal
*Bramble Knoll
*Marlow Park
*Seawall Moorings
*The Esplanade Walk
*Tolly Brook
The important streets are:
*The Esplanade Walk
*Harcourt Street
*Pembrey Street
*Wexley Street
*Cobb/Lyall/Vane Streets (One road, it just changes names)
*Redding Street
(Note: The Esplanade Walk refers to a street and a long beach frontage)
I have created a Google Maps map with all of these points labelled:
https://maps.examplemaps.com.au/maps/ms?
msid=381726450019384756201.0007a1b3d4e5f6a7b8c9d&
msa=0&ll=-20.118734,147.302918&
spn=0.03117,0.048825
Target Market(s)
Backpackers, students, short-term residents and seasonal workers
Industry/Entity Type
Marketing

```html
<!DOCTYPE html>
<html lang="en">
<head>
<meta charset="utf-8">
<title>Wanderbunk Lodge – Tri-fold Flyer (Inside)</title>
<link rel="stylesheet" href="https://fonts.googleapis.com/css2?family=Pinyon+Script&family=Quicksand:wght@300;400&display=swap">
<style>
  :root {
    --backdrop: #2e2e2e;
    --plum: #6a2a52;
    --plum-deep: #5a2346;
    --plum-dark: #4e1d3d;
    --ink: #141419;
    --map-plum: #5c2a4c;
    --map-dark: #231c26;
    --label-muted: #7a4f6c;
    --text-light: #f4f1f3;
  }
  * { margin: 0; padding: 0; box-sizing: border-box; }
  html, body { width: 1200px; height: 844px; overflow: hidden; }
  body {
    background: var(--backdrop);
    font-family: "Quicksand", sans-serif;
    font-weight: 400;
    color: var(--text-light);
    position: relative;
  }
  .flyer {
    position: absolute;
    left: 52px; top: 33px;
    width: 1090px; height: 767px;
    background: var(--ink);
    overflow: hidden;
  }
  .flyer__shapes { position: absolute; inset: 0; }
  .block { position: absolute; font-size: 11px; line-height: 14px; }
  .heading {
    font-family: "Pinyon Script", cursive;
    font-weight: 400;
    font-size: 24px;
    line-height: 28px;
  }
  .heading--list { margin-bottom: 6px; }
  .list { list-style: none; }
  .list li { line-height: 15.6px; }
  .list li::before { content: "• "; }
  .list .indent { padding-left: 7px; }
  .list .indent::before { content: ""; }

  .offer { left: 66px; top: 90px; width: 240px; }
  .attractions { left: 88px; top: 262px; width: 280px; }
  .facilities { left: 466px; top: 52px; width: 230px; }
  .accommodation { left: 444px; top: 386px; width: 236px; }
  .location { left: 816px; top: 146px; width: 210px; line-height: 14px; }

  .map {
    position: absolute; left: 734px; top: 0;
    width: 356px; height: 205px;
    background:
      radial-gradient(ellipse 120px 80px at 230px 100px, var(--map-plum) 0%, rgba(92,42,76,0.55) 55%, rgba(92,42,76,0) 100%),
      linear-gradient(180deg, var(--map-dark) 0%, #1d1920 70%, var(--ink) 100%);
  }
  .map__pin { position: absolute; left: 852px; top: 74px; }

  .contact {
    position: absolute; left: 766px; top: 455px; width: 294px;
    text-align: center; font-size: 10.4px; line-height: 12.4px;
    font-style: normal;
  }
  .contact__label { color: var(--label-muted); }
  .contact__title { color: var(--label-muted); margin-bottom: 10px; }

  .gallery {
    position: absolute; left: 0; top: 605px;
    width: 1090px; height: 110px;
    display: flex;
  }
  .gallery__photo { height: 100%; }
</style>
</head>
<body>
<main class="flyer">
  <svg class="flyer__shapes" width="1090" height="767" viewBox="0 0 1090 767" aria-hidden="true">
    <rect x="0" y="0" width="734" height="580" fill="var(--plum)"/>
    <path d="M0 0 H420 C360 60 200 90 0 110 Z" fill="var(--plum-deep)"/>
    <path d="M330 0 H430 C520 120 620 300 734 400 V520 C600 380 480 150 330 0 Z" fill="var(--plum-deep)" opacity="0.8"/>
    <path d="M734 0 V60 C640 50 560 30 520 0 Z" fill="var(--plum-dark)" opacity="0.6"/>
    <path d="M0 527 C120 505 260 500 360 520 C400 528 420 540 436 548 C460 540 520 532 560 540 L734 560 L734 767 L0 767 Z" fill="var(--ink)"/>
    <path d="M436 548 C470 520 520 470 560 420 C530 480 480 530 450 558 Z" fill="var(--plum)"/>
  </svg>

  <div class="map" role="img" aria-label="Simplified street map of the area around Wanderbunk Lodge Tidewell, showing main roads and the hostel block"></div>
  <svg class="map__pin" width="12" height="20" viewBox="0 0 12 20" aria-hidden="true">
    <path d="M6 0 C2.7 0 0 2.7 0 6 C0 10 6 20 6 20 C6 20 12 10 12 6 C12 2.7 9.3 0 6 0 Z" fill="#ffffff"/>
  </svg>

  <section class="block offer">
    <h2 class="heading">We offer</h2>
    <p>premium accommodation at an afordable price for international students, travellers and seasonal workers in a fantastic location ideal for exploring all that Harrowbay and North Coralia have to offer.</p>
  </section>

  <section class="block attractions">
    <h2 class="heading heading--list">Local attractions ...</h2>
    <ul class="list">
      <li>Pelican Cay</li>
      <li>SS Merrowind Shipwreck Dive</li>
      <li>The Esplanade Walk Foreshore and Rockpool</li>
      <li>Kestrel Wildlife Sanctuary</li>
      <li>ReefWorks Aquarium</li>
      <li>Heron Creek Falls</li>
      <li>Wyndle Falls</li>
      <li>Arrowfern Rainforest Village</li>
      <li>Lakeside Pools and Riverwalk</li>
    </ul>
  </section>

  <section class="block facilities">
    <h2 class="heading heading--list">Facilities ...</h2>
    <ul class="list">
      <li>Computer and Wi-Fi Internet access</li>
      <li>Fully-equipped modern kitchens</li>
      <li>Completely renovated bathrooms</li>
      <li>Crisp and clean bed linen</li>
      <li>On-site laundry facilities</li>
      <li>Free luggage storage service</li>
      <li>Air-conditioned bedrooms</li>
      <li>Large open common areas</li>
      <li>Of-street parking</li>
      <li>Close to regular public transport</li>
      <li>Transfers to and from the Pelican Cay</li>
      <li class="indent">ferry and other transport hubs</li>
      <li>Push bike hire</li>
      <li>Book exchange</li>
      <li>BBQ area</li>
    </ul>
  </section>

  <section class="block accommodation">
    <h2 class="heading">Accommodation ...</h2>
    <p>We have spacious shared and private rooms that sleep 1 to 10 people. Individual and group bookings are welcome with nightly, weekly and monthly rates available.</p>
  </section>

  <section class="block location">
    <h2 class="heading">Location ...</h2>
    <p>We are located at 8 The Crescent, Linden Park which is just of Corrigan Road.How to get to our hostel ...We ofer a free pick-up service from the train station, Pelican Cay ferry terminal, and the Swiftline and Coastlink bus stations between the hours of 11 a.m. and 7 p.m. Please contact us 24 hours prior to your arrival to arrange this.<br>
    Outside of these hours we are convieniently located on the main local bus route. From the City Arcade: the public bus route #200 or #201 can take you to the Fernley Terrace bus stop which is just 30 metres from our hostel. A taxi service also runs late at night.</p>
  </section>

  <address class="contact">
    <p class="contact__title">Contact ...</p>
    <p><span class="contact__label">Phone:</span> +61 (0)7 5550 1234</p>
    <p><span class="contact__label">Mobile:</span> 0400 555 019</p>
    <p class="contact__label">Web:</p>
    <p>www.harbourlarkstays.com.au</p>
    <p class="contact__label">E-mail:</p>
    <p>tidewell@harbourlarkstays.com.au</p>
  </address>

  <div class="gallery">
    <div class="gallery__photo" style="width:172px;background:linear-gradient(#cfd2d6,#6b5a48);" role="img" aria-label="Outdoor BBQ patio with timber furniture"></div>
    <div class="gallery__photo" style="width:148px;background:linear-gradient(#e8e6e8,#c97a3c);" role="img" aria-label="Common dining room with white tables"></div>
    <div class="gallery__photo" style="width:58px;background:linear-gradient(#7a2d66,#4a1d40);" role="img" aria-label="Purple gym door sign"></div>
    <div class="gallery__photo" style="width:92px;background:linear-gradient(#efe7b8,#b9b3a0);" role="img" aria-label="Gym room with weight machine"></div>
    <div class="gallery__photo" style="width:154px;background:linear-gradient(#f1f1f3,#c46a78);" role="img" aria-label="Hallway with purple door and lounge chair"></div>
    <div class="gallery__photo" style="width:162px;background:linear-gradient(#c23c78,#c96860);" role="img" aria-label="Computer room with desks"></div>
    <div class="gallery__photo" style="width:152px;background:linear-gradient(#f4f4f2,#cfc4a8);" role="img" aria-label="Renovated bathroom with shower and basin"></div>
    <div class="gallery__photo" style="width:152px;background:linear-gradient(#f3ecd0,#c94f58);" role="img" aria-label="Shared bedroom with bunk beds"></div>
  </div>
</main>
</body>
</html>
```